Charter boat business marketing piece

I need a .pdf for a 6 x 11 piece that will be used as a give-away marketing piece for hotel concierges in the Clearwater/Tarpon Springs, FL area. It will be printed on glossy postcard paper stock. I provide private, captained boat charters for small groups (max 6). The trips on my 24 foot Gullwing Baycraft may include: watching wildlife like dolphins, manatees, sea turtles, birds and other wildlife, sunset cruises, barrier island tours, secluded beach walks, shelling, river cruises, sightseeing, water skiing and inner tubing, etc. People like to use my boat tour for photo shoots, wildlife photography, romantic dates, birthday parties, and weddings/anniversaries, etc. The biggest selling point for my service is that is is private and not with lots of other people like most boat trips sold in the area. I typically will have a small group of friends or a family who want to have a personalized day on the water. I try to provide a higher end experience. The current fees are $250 for half day (4 hours) and $450 for a full day (hours). If people are having lots of fun, they can extend their trips for $75/hour. I have been using some P2P sites for getting business, but I would like to have a marketing piece that I can give to hotel/resort concierges to give to their guests. But I want it to be a nicer/more effective marketing piece (and different) than the typical fishing charter or group charter brochures. You can see more pictures and information about my boat and services on the P2P site here: https://www.marinohire.net/boat-rentals/clearwater-fl/8394
What I am envisioning is a double sided 6 x 11 glossy finish postcard. I don't have a working name for my business yet so a generic name/logo can be inserted into the artwork for now. I would like some feedback on the type of pictures I should get. I have access to professional photography and am ok with using some purchase stock photos if necessary.

Target Market(s)

Hotel/resort guests that are looking to experience more adventure while on their trip to Clearwater/Tarpon Springs area. People who don't mind spending a little more to get a private boat ride with a captain (me). I make it easy for them so they don't have to know how to drive a boat, don't run the risk of hurting the boat or themselves, can sit back and relax and even drink alcohol without worrying about anything. Plus I know exactly where to take them to show them the sights.

Industry/Entity Type

Business

Colors

Designer to choose colors to be used in the design.

Requirements
Must have
• An effective and attractive design including eye catching photography and call to action.
• The correct information about rates, services and contact/reservation information.
Nice to have
• Not sure
Should not have
• I don't want this to look like one of the other touristy brochures. I want it to look better and work better.

```html
<!DOCTYPE html>
<html lang="en">
<head>
<meta charset="utf-8">
<title>Captained Boat Charters – Postcard</title>
<link rel="stylesheet" href="https://fonts.googleapis.com/css2?family=Bebas+Neue&family=Oswald:wght@500&family=Arimo:wght@400;700&display=swap">
<style>
  :root {
    --teal: #14a89e;
    --teal-dark: #0b7e77;
    --white: #ffffff;
    --ink: #000000;
    --sky: #9cc9e6;
    --sea: #3f6a86;
    --ocean-blue: #4d8fb0;
    --lagoon: #2e9fbf;
  }
  * { margin: 0; padding: 0; box-sizing: border-box; }
  html, body { width: 999px; height: 1200px; overflow: hidden; background: var(--ink); }
  body { position: relative; font-family: "Arimo", Arial, sans-serif; color: var(--white); }

  .card { position: absolute; left: 28px; width: 942px; overflow: hidden; }
  .card--front { top: 83px; height: 515px; }
  .card--back { top: 615px; height: 513px; background: var(--white); }
  .card svg.shapes { position: absolute; inset: 0; }

  .front-title {
    position: absolute; left: 42px; top: 38px;
    font-family: "Bebas Neue", "Oswald", sans-serif;
    font-size: 64px; line-height: 58px; letter-spacing: 0.5px;
  }
  .front-subhead { position: absolute; left: 42px; font-weight: 700; font-size: 19px; line-height: 24px; }
  .front-subhead--wildlife { top: 192px; }
  .front-subhead--other { top: 325px; }

  .arrow-list { position: absolute; list-style: none; }
  .arrow-list li { position: relative; padding-left: 20px; }
  .arrow-list li::before {
    content: ""; position: absolute; left: 3px; top: 50%;
    width: 9px; height: 9px; transform: translateY(-50%);
    background: var(--white);
    clip-path: polygon(0 0, 55% 0, 100% 50%, 55% 100%, 0 100%, 40% 50%);
  }
  .arrow-list--wildlife { left: 44px; top: 250px; font-size: 13px; line-height: 17px; }
  .arrow-list--trips { left: 44px; top: 351px; font-size: 13px; line-height: 17.2px; }

  .boat-model {
    position: absolute; left: 270px; top: 200px; width: 166px;
    text-align: center; font-weight: 700; font-size: 27px; line-height: 35px;
  }

  .back-heading {
    position: absolute; left: 40px; top: 34px;
    font-family: "Oswald", "Bebas Neue", sans-serif; font-weight: 500;
    font-size: 22px; line-height: 28px;
  }
  .arrow-list--uses { left: 40px; top: 74px; font-size: 18px; line-height: 22.3px; }
  .arrow-list--uses li::before { width: 10px; height: 10px; }

  .selling-point {
    position: absolute; left: 43px; top: 197px; width: 410px;
    font-size: 12.4px; line-height: 17px;
  }

  .price-box {
    position: absolute; top: 330px; width: 173px; height: 122px;
    background: var(--teal-dark); border-radius: 10px;
    text-align: center; font-weight: 700;
  }
  .price-box--rates { left: 39px; padding-top: 5px; font-size: 11px; line-height: 13px; }
  .price-box--extend { left: 223px; padding-top: 18px; font-size: 11.5px; line-height: 14px; }
  .price-box .amount { font-size: 33px; line-height: 32px; }
  .price-box .amount--extend { display: inline-block; margin-top: 8px; font-size: 33px; line-height: 36px; }
  .price-box .unit { font-size: 11px; }

  .stamp-box { position: absolute; left: 814px; top: 37px; width: 100px; height: 100px; background: var(--ink); }
  .address-line { position: absolute; left: 585px; width: 295px; height: 3px; background: var(--ink); }
</style>
</head>
<body>

<section class="card card--front">
  <svg class="shapes" width="942" height="515" viewBox="0 0 942 515">
    <defs>
      <linearGradient id="boatPhotoTone" x1="0" y1="0" x2="0" y2="1">
        <stop offset="0" stop-color="var(--sky)"/>
        <stop offset="0.18" stop-color="#b8d6e8"/>
        <stop offset="0.2" stop-color="var(--sea)"/>
        <stop offset="1" stop-color="#2c4f68"/>
      </linearGradient>
      <linearGradient id="whaleTone" x1="0" y1="0" x2="0" y2="1">
        <stop offset="0" stop-color="#a9c3cf"/>
        <stop offset="1" stop-color="var(--ocean-blue)"/>
      </linearGradient>
      <linearGradient id="manateeTone" x1="0" y1="0" x2="0" y2="1">
        <stop offset="0" stop-color="#3b8fb0"/>
        <stop offset="1" stop-color="var(--lagoon)"/>
      </linearGradient>
    </defs>
    <rect role="img" aria-label="Photo of the charter deck boat speeding across the bay with guests aboard" x="0" y="0" width="942" height="515" fill="url(#boatPhotoTone)"/>
    <polygon role="img" aria-label="Photo of a whale tail rising from the sea" points="340,0 632,0 487,252" fill="url(#whaleTone)"/>
    <polygon role="img" aria-label="Photo of manatees swimming in clear water" points="340,515 614,515 487,252" fill="url(#manateeTone)"/>
    <polyline points="630,-2 487,252 612,517" fill="none" stroke="var(--teal-dark)" stroke-width="10"/>
    <polyline points="352,-2 478,250 347,517" fill="none" stroke="var(--teal-dark)" stroke-width="8"/>
    <polygon points="0,0 352,0 478,250 347,515 0,515" fill="var(--teal)"/>
  </svg>

  <h1 class="front-title">Captained Boat<br>Charters</h1>

  <h2 class="front-subhead front-subhead--wildlife">Watching<br>Wildlife like</h2>
  <ul class="arrow-list arrow-list--wildlife">
    <li>Dolphins</li>
    <li>Manatees</li>
    <li>Sea Turtles</li>
    <li>Birds</li>
  </ul>

  <h2 class="front-subhead front-subhead--other">and other Wildlife</h2>
  <ul class="arrow-list arrow-list--trips">
    <li>Sunset Cruises</li>
    <li>Barrier Island Tours</li>
    <li>Secluded Beach Walks</li>
    <li>Shelling</li>
    <li>River Cruises</li>
    <li>Sightseeing</li>
    <li>Water Skiing</li>
    <li>And Inner Tubing, Etc.</li>
  </ul>

  <p class="boat-model">24 foot Gullwing Baycraft</p>
</section>

<section class="card card--back">
  <svg class="shapes" width="942" height="513" viewBox="0 0 942 513">
    <polygon points="0,0 392,0 527,267 397,513 0,513" fill="var(--teal-dark)"/>
    <polygon points="0,0 374,0 510,267 380,513 0,513" fill="var(--teal)"/>
  </svg>

  <h2 class="back-heading">People like to use my boat tour for</h2>
  <ul class="arrow-list arrow-list--uses">
    <li>Photo Shoots</li>
    <li>Wildlife Photography</li>
    <li>Romantic Dates</li>
    <li>Birthday Parties</li>
    <li>And Weddings/anniversaries, Etc.</li>
  </ul>

  <p class="selling-point">The biggest selling point for my service is that is is private and not with lots of other people like most boat trips sold in the area. I typically will have a small group of friends or a family who want to have a personalized day on the water. I try to provide a higher end experience.</p>

  <div class="price-box price-box--rates">
    The current fees are<br>
    <span class="amount">$250</span><br>
    for half day (4 hours)<br>
    and<span class="amount">$450</span><br>
    for a full day (hours).
  </div>

  <div class="price-box price-box--extend">
    If people are having lots<br>of fun, they can extend<br>their trips for<br>
    <span class="amount--extend">$75</span> <span class="unit">/hour.</span>
  </div>

  <div class="stamp-box"></div>
  <div class="address-line" style="top:335px"></div>
  <div class="address-line" style="top:395px"></div>
  <div class="address-line" style="top:455px"></div>
</section>

</body>
</html>
```